Fatigued and Overloaded by COVID Messages? We need original illustrations to show that.

Everywhere you look there are messages about COVID. That is leading many people to feel fatigued and overloaded by the messages.

We surveyed U.S. adults March 20th - 24th, 2020 and measured message fatigue, information overload, perceived repetition, and perceived exaggeration. Here is how participants responded:

When it comes to coronavirus . . .
55% feel exhausted by all the messages.
54% feel overloaded by the amount of information.
51% feel that the messages are repetitive.
47% feel like messages exaggerate how bad it is.

In other words, almost half of U.S. adults show signs of message fatigue, information overload, perceived message repetition, and perceived message exaggeration.

We will continue to survey 400 adults every week for the next 16 weeks. Each time we will measure message fatigue, information overload, perceived repetition, and perceived exaggeration. We expect that it will increase over time.

What are we looking for? We need innovative and original illustrations that attempt to communicate these findings. The illustrations would visualize message fatigue, information overload, perceived message repetition, and perceived message exaggeration.

What sort of visual are we looking for? Our preference is for an original illustration (or set of illustrations). Our preference is for creative and powerful illustrations, but we are also open to the creative and well-executed infographics.

We need these images fast . We will award monetary prizes to the 3 best designs. If we like more than that, then we might purchase more (e.g., in past contests, we have purchased as many as 30 designs).

What we will need:
(1) The illustrations must be original and we will need the photoshop and/or illustrator files for all artwork. (By original, we mean that the illustrations are 100% created by you. Our organization requires that we utilize only original illustrated work. We have had issues with free imagery being pirated and reposted as free. We sidestep that issue by just having everything created.)

(2) The illustration should say, somewhere: "Based on a survey of 400 U.S. adults conducted March 20 - 24th, 2020."

(3) We will have almost 4 months worth of data by the time this is done. In other words, the illustrations might be able to help us present that weekly data.

(4) We have conducted other Artvendo projects. It might be helpful to examine designs we liked in the past. For example, here is another COVID project we just finished:

https://jobs.artvendo-example.com/job/5162048

Target Market(s)

U.S. adults

Requirements
Must have
• Original illustrations. Mobile friendly design. People will view this on their smartphones.
Nice to have
• A design that we can use to communicate the data across time.

```html
<!DOCTYPE html>
<html lang="en">
<head>
<meta charset="utf-8">
<title>How Americans Feel When It Comes to Coronavirus</title>
<link rel="stylesheet" href="https://fonts.googleapis.com/css2?family=Poppins:wght@600;700;800&display=swap">
<style>
  :root {
    --ink: #1e2d35;
    --paper: #ffffff;
    --pale-lime: #eefbd0;
    --lime: #a8f20c;
    --footer-lime: #e4f7bf;
    --footer-grey: #8d9b87;
  }
  * { margin: 0; padding: 0; box-sizing: border-box; }
  html, body { width: 1200px; height: 2722px; overflow: hidden; background: var(--paper); }
  body { font-family: "Poppins", sans-serif; color: var(--ink); }
  .poster { position: relative; width: 1200px; height: 2722px; overflow: hidden; background: var(--paper); }

  .halo { position: absolute; left: 97px; top: 337px; width: 1460px; height: 1460px; border-radius: 50%; background: var(--pale-lime); }
  .alert-mark { position: absolute; left: 1015px; top: 112px; width: 130px; height: 240px; }

  .headline { position: absolute; left: 120px; top: 76px; font-weight: 700; text-transform: uppercase; }
  .headline-lead { font-size: 66px; line-height: 75px; letter-spacing: -1px; }
  .headline-topic { position: absolute; left: 120px; top: 212px; font-size: 112px; line-height: 112px; font-weight: 700; letter-spacing: -3px; }
  .headline-dots { position: absolute; left: 122px; top: 340px; font-size: 40px; line-height: 40px; font-weight: 800; letter-spacing: 2px; }

  .virus-art { position: absolute; left: 75px; top: 453px; width: 400px; height: 384px; border-radius: 190px 190px 0 0; background: var(--ink); }

  .stats-panel { position: absolute; left: 0; top: 837px; width: 1200px; height: 1885px; background: var(--ink); }

  .person-art { position: absolute; left: 581px; top: 453px; width: 518px; height: 630px; border-radius: 220px 220px 140px 140px; background: linear-gradient(160deg, var(--lime) 0%, #d9f98f 45%, var(--paper) 100%); }

  .stat-value, .stat-label { position: absolute; color: var(--paper); font-weight: 700; white-space: nowrap; }
  .stat-value { left: 96px; font-size: 245px; line-height: 245px; letter-spacing: -6px; }
  .stat-label { left: 101px; font-size: 59px; line-height: 61px; letter-spacing: -0.5px; text-transform: uppercase; }

  .source { position: absolute; left: 0; width: 1200px; text-align: center; font-size: 26px; line-height: 32px; font-weight: 600; text-transform: uppercase; letter-spacing: 0.5px; }
  .source-survey { top: 2558px; color: var(--footer-lime); }
  .source-note { top: 2594px; color: var(--footer-grey); }
</style>
</head>
<body>
<main class="poster">
  <div class="halo"></div>

  <svg class="alert-mark" viewBox="0 0 130 240" aria-hidden="true">
    <path d="M52 10 Q60 0 76 4 L112 14 Q128 20 122 36 L64 170 Q56 182 46 176 Q38 172 40 160 Z" fill="#e6f7bf"/>
    <circle cx="36" cy="210" r="26" fill="#e6f7bf"/>
  </svg>

  <h1 class="headline"><span class="headline-lead">How Americans feel<br>when it comes</span></h1>
  <div class="headline-topic">CORONAVIRUS</div>
  <div class="headline-dots">...</div>

  <div class="virus-art" role="img" aria-label="Illustration of dark coronavirus particles"></div>

  <section class="stats-panel" aria-label="Survey results"></section>

  <div class="person-art" role="img" aria-label="Illustration of a stressed person in a lime sweater holding their head"></div>

  <div class="stat-value" style="top:912px">55%</div>
  <p class="stat-label" style="top:1172px">Feel exhausted by all the<br>messages</p>

  <div class="stat-value" style="top:1316px; left:112px">54%</div>
  <p class="stat-label" style="top:1556px">Feel overloaded by the<br>amount of information</p>

  <div class="stat-value" style="top:1723px; left:112px">51%</div>
  <p class="stat-label" style="top:1961px">Feel that the messages are<br>repetitive.</p>

  <div class="stat-value" style="top:2096px; left:106px">47%</div>
  <p class="stat-label" style="top:2335px">Feel like messages<br>exaggerate how bad it is.</p>

  <p class="source source-survey">Survey of U.S. adults (N = 400) conducted March 20th - 24th, 2020</p>
  <p class="source source-note">Percent of Americans intending to engage in social distancing</p>
</main>
</body>
</html>
```